Online-Marketing Material für ambulanter Pflegedienst
Zielgruppe
Unser Unternehmen, Lindenhain, ist ein ambulanter Pflegedienst, der sich darauf spezialisiert hat, individuelle und herzliche Pflege direkt in den eigenen vier Wänden unserer Klienten in Nürnberg und Umgebung anzubieten. Unser Hauptziel ist es, die Lebensqualität und Unabhängigkeit unserer Klienten zu fördern und zu erhalten, indem wir professionelle Pflege und Unterstützung bieten.
Unsere Dienstleistungen reichen von der häuslichen Krankenpflege über Palliative Care bis hin zur Beratung, wobei wir einen ganzheitlichen Ansatz verfolgen, um den individuellen Bedürfnissen und Wünschen jedes Klienten gerecht zu werden.
Unsere Zielgruppe sind vor allem ältere Menschen, die Unterstützung im Alltag benötigen, sowie Personen jeden Alters, die aufgrund von Krankheit oder Behinderung Pflege und Assistenz benötigen. Wir arbeiten eng mit den Familien unserer Klienten zusammen, um sicherzustellen, dass die von uns angebotene Pflege und Unterstützung auf die persönlichen Anforderungen und Vorlieben jedes Einzelnen abgestimmt ist.
Aufgabenstellung
Liebes Design-Team,
wir möchten eine Serie von Bannern erstellen lassen, die die Herzlichkeit und Fürsorge unseres ambulanten Pflegedienstes visualisieren. Jedes Banner soll einen anderen Schwerpunkt unserer Dienstleistungen präsentieren: Palliativpflege, Krankenpflege, Grundpflege sowie Betreuung und Hauswirtschaft.
Für die Gestaltung möchten wir gerne auf freundliche und liebevolle Vectorgrafiken setzen, die vor allem ältere und pflegebedürftige Menschen ansprechen. Die Botschaft sollte klar und einladend sein, um die Wärme und Unterstützung zu kommunizieren, die wir unseren Klienten täglich bieten.
Hier sind einige spezifische Anforderungen für jedes Banner:
Banner müssen für Chatterly Werbung gestaltet werden. (940x788px) FREUNDLICHE UND RUNDE FORMEN sind erwünscht.
Banner 1: Palliativpflege - „wo Geborgenheit zuhause ist“
Untertitel: Fürsorgliche Hände, die in schwierigen Zeiten trösten
Spezialisierte Pflege für Schmerzmanagement und Symptomlinderung
Emotionaler Beistand und Unterstützung für Patienten und ihre Familien
Personalisierte Betreuung, die auf die Bedürfnisse jedes Einzelnen eingeht
Banner 2: Krankenpflege - „wo Geborgenheit zuhause ist“
Untertitel: Fachmännische Pflege, die Genesung unterstützt
Qualifizierte Krankenpflege und Medikamentenmanagement zu Hause
Professionelle Wundversorgung und nachoperative Pflege
Individuelle Pflegepläne zur Förderung der Gesundheit und des Wohlbefindens
Banner 3: Grundpflege - „wo Geborgenheit zuhause ist“
Untertitel: Tägliche Handreichungen, die das Leben erleichtern
Unterstützung bei der Körperpflege, Mobilität und Ernährung
Empathische Betreuung zur Bewahrung der Würde und Unabhängigkeit
Personalisierte Unterstützung, die das tägliche Leben erleichtert
Banner 4: Betreuung und Hauswirtschaft - „wo Geborgenheit zuhause ist“
Unte..

```html
<!DOCTYPE html>
<html lang="de">
<head>
<meta charset="utf-8">
<title>Lindenhain – Bannerserie</title>
<link href="https://fonts.googleapis.com/css2?family=Roboto+Condensed:wght@400;700&family=Roboto:wght@400&display=swap" rel="stylesheet">
<style>
  :root{
    --page:#ffffff;
    --panel:#eef5fb;
    --soft-blue:#dcecf8;
    --band:#3b86c8;
    --deep-blue:#1b5faa;
    --orange:#f4a51c;
    --sun:#f6b81a;
    --soft-yellow:#fde7b2;
    --ink:#222428;
    --white:#ffffff;
  }
  *{box-sizing:border-box;margin:0;padding:0}
  html,body{width:1200px;height:938px;overflow:hidden;background:var(--page)}
  .board{position:relative;width:1200px;height:938px}
  .banner{
    position:absolute;width:449px;height:376px;overflow:hidden;
    background:var(--panel);
    box-shadow:0 1px 4px rgba(0,0,0,.18);
  }
  .banner--palliativ{left:111px;top:67px}
  .banner--kranken{left:639px;top:67px}
  .banner--grund{left:111px;top:494px}
  .banner--haus{left:639px;top:494px}

  .deco{position:absolute;border-radius:50%}
  .deco--corner{left:-58px;top:-48px;width:116px;height:116px;background:var(--soft-blue)}
  .deco--sun{left:0;top:348px;width:76px;height:76px;background:var(--soft-yellow)}
  .deco--wave{left:300px;top:310px;width:260px;height:200px;background:var(--soft-blue)}

  .brand{position:absolute;left:10px;top:62px;width:200px;text-align:center}
  .brand__row{display:flex;align-items:center;justify-content:center;gap:6px}
  .brand__dot{width:14px;height:14px;border-radius:50%;background:var(--sun)}
  .brand__name{
    font-family:"Roboto Condensed",sans-serif;font-weight:700;font-size:25px;
    letter-spacing:.5px;color:var(--deep-blue);line-height:1;
  }
  .brand__tagline{
    margin-top:2px;font-family:"Roboto",sans-serif;font-size:9px;color:var(--band);
  }

  .title-band{
    position:absolute;left:1px;top:117px;width:209px;
    background:var(--band);border-bottom:3px solid var(--orange);
    padding:4px 10px 6px;color:var(--white);
    font-family:"Roboto Condensed",sans-serif;
  }
  .title-band__title{font-weight:700;font-size:25px;line-height:1;letter-spacing:.2px}
  .title-band__sub{font-weight:400;font-size:13.5px;line-height:1.2;margin-top:3px;letter-spacing:.1px;white-space:nowrap}

  .copy{position:absolute;left:12px;width:196px}
  .copy__heading{
    font-family:"Roboto Condensed",sans-serif;font-weight:700;font-size:17px;
    line-height:21.5px;color:var(--ink);text-transform:uppercase;white-space:nowrap;
  }
  .copy__text{
    font-family:"Roboto",sans-serif;font-size:10.2px;line-height:14.3px;
    color:var(--ink);margin-top:4px;
  }

  .photo{
    position:absolute;left:211px;top:35px;width:228px;height:320px;
    border-radius:56px 0 70px 0;
    box-shadow:4px 3px 0 var(--deep-blue);
  }
  .photo--tree{background:linear-gradient(110deg,#c58a4a 0%,#6b5142 25%,#8a6c58 55%,#b0523e 62%,#7a6050 80%,#5e4a3e 100%)}
  .photo--pressure{background:linear-gradient(120deg,#e8d6d6 0%,#f3e7e4 35%,#c9b2ae 55%,#2c3440 70%,#e6c8bd 100%)}
  .photo--help{background:linear-gradient(120deg,#3b3230 0%,#e0906b 30%,#f1ede8 55%,#8a5a3c 70%,#2f6f7a 100%)}
  .photo--home{background:linear-gradient(120deg,#f4efe4 0%,#e7dccb 35%,#c98a6a 55%,#f7f3ee 75%,#d9cfc4 100%)}
</style>
</head>
<body>
<main class="board">

  <section class="banner banner--palliativ">
    <div class="deco deco--corner"></div>
    <div class="deco deco--sun"></div>
    <div class="deco deco--wave"></div>
    <div class="brand">
      <div class="brand__row"><span class="brand__dot"></span><span class="brand__name">LINDENHAIN</span></div>
      <p class="brand__tagline">wo Geborgenheit zuhause ist!</p>
    </div>
    <div class="title-band">
      <h2 class="title-band__title">PALLIATIVPFLEGE</h2>
      <p class="title-band__sub">WO GEBORGENHEIT ZUHAUSE IST</p>
    </div>
    <div class="copy" style="top:191px">
      <h3 class="copy__heading">Fürsorgliche Hände<br>die in schwierigen<br>Zeiten trösten</h3>
      <p class="copy__text">Spezialisierte Pflege für Schmerzman&shy;agement und Symptomlinderung Emotionaler Beistand und Unterstütz&shy;ung für Patienten und ihre Familien Personalisierte Betreuung, die auf die Bedürfnisse jedes Einzelnen eingeht</p>
    </div>
    <div class="photo photo--tree" role="img" aria-label="Kinderhände umarmen einen Baumstamm mit aufgemaltem roten Herz"></div>
  </section>

  <section class="banner banner--kranken">
    <div class="deco deco--corner"></div>
    <div class="deco deco--sun"></div>
    <div class="deco deco--wave"></div>
    <div class="brand">
      <div class="brand__row"><span class="brand__dot"></span><span class="brand__name">LINDENHAIN</span></div>
      <p class="brand__tagline">wo Geborgenheit zuhause ist!</p>
    </div>
    <div class="title-band">
      <h2 class="title-band__title">KRANKENPFLEGE</h2>
      <p class="title-band__sub">WO GEBORGENHEIT ZUHAUSE IST</p>
    </div>
    <div class="copy" style="top:191px">
      <h3 class="copy__heading">Fachmännische<br>Pflege, die Genesung<br>unterstützt</h3>
      <p class="copy__text">Qualifizierte Krankenpflege und Medika&shy;mentenmanagement zu Hause Profes&shy;sionelle Wundversorgung und nachop&shy;erative Pflege Individuelle Pflegepläne zur Förderung der Gesundheit und des Wohlbefindens</p>
    </div>
    <div class="photo photo--pressure" role="img" aria-label="Pflegekraft misst den Blutdruck am Arm einer Patientin"></div>
  </section>

  <section class="banner banner--grund">
    <div class="deco deco--corner"></div>
    <div class="deco deco--sun"></div>
    <div class="deco deco--wave"></div>
    <div class="brand">
      <div class="brand__row"><span class="brand__dot"></span><span class="brand__name">LINDENHAIN</span></div>
      <p class="brand__tagline">wo Geborgenheit zuhause ist!</p>
    </div>
    <div class="title-band">
      <h2 class="title-band__title">GRUNDPFLEGE</h2>
      <p class="title-band__sub">WO GEBORGENHEIT ZUHAUSE IST</p>
    </div>
    <div class="copy" style="top:185px">
      <h3 class="copy__heading">Tägliche<br>Handreichungen, die<br>das Leben erleichtern</h3>
      <p class="copy__text">Unterstützung bei der Körperpflege, Mobilität und Ernährung Empathische Betreuung zur Bewahrung der Würde und Unabhängigkeit Personalisierte Unterstützung, die das tägliche Leben erleichtert</p>
    </div>
    <div class="photo photo--help" role="img" aria-label="Junge Frau hilft einem älteren Herrn mit Gehstock im Sessel"></div>
  </section>

  <section class="banner banner--haus">
    <div class="deco deco--corner"></div>
    <div class="deco deco--sun"></div>
    <div class="deco deco--wave"></div>
    <div class="brand">
      <div class="brand__row"><span class="brand__dot"></span><span class="brand__name">LINDENHAIN</span></div>
      <p class="brand__tagline">wo Geborgenheit zuhause ist!</p>
    </div>
    <div class="title-band">
      <h2 class="title-band__title">BETREUUNG UND<br>HAUSWIRTSCHAFT</h2>
      <p class="title-band__sub">WO GEBORGENHEIT ZUHAUSE IST</p>
    </div>
    <div class="copy" style="top:214px">
      <h3 class="copy__heading" style="font-size:16px;line-height:19px">Ihr Zuhause, liebevoll<br>gepflegt undorganisiert</h3>
      <p class="copy__text">Haushaltshilfe, Einkaufen und Mahl&shy;zeitenvorbereitung Organisation und Säuberung des Wohnraums zur Förderung einer angenehmen Umge&shy;bung Unterstützung bei täglichen Auf&shy;gaben für ein selbstbestimmtes Leben</p>
    </div>
    <div class="photo photo--home" role="img" aria-label="Lächelnde Seniorin mit Rollator in ihrer hellen Wohnung, im Hintergrund eine Haushaltshilfe"></div>
  </section>

</main>
</body>
</html>
```